bizcards, stationary, envelopes, powerpoint template, invoice template, polo shirts, email template
ms word templates of stationary also please
bizcards, stationary, envelopes,  powerpoint template, invoice template, polo shirts, email template - Aviation
Creative Brief
Professional
Samuel K Orlowski
Founder
The Halvern Tower 482 Tamsin Ridge Rd. Suite 210 Westlake, OH 44718
sorlowski@meridowair.example
www.meridowair.example
Air Carrier #4RXB519T
Only use the colors and font of our logo. Our tag line "THE SPEED IS YOURS" can be used in a creative way of your thoughts.
wide ope, maybe a Skyvalent Jet watermark, the tag line, the tag line & logo, etc.

```html
<!DOCTYPE html>
<html lang="en">
<head>
<meta charset="utf-8">
<title>Meridow Air Charter – Business Card</title>
<link rel="stylesheet" href="https://fonts.googleapis.com/css2?family=Arimo:wght@400;700&display=swap">
<style>
  :root {
    --backdrop: #ecebe8;
    --card: #ffffff;
    --brand-green: #8cc63f;
    --brand-green-dark: #6fa52a;
    --brand-grey: #6d6e71;
    --text-grey: #8a8b8e;
    --band-grey: #7b7c7f;
  }
  html, body {
    margin: 0;
    padding: 0;
    width: 1200px;
    height: 935px;
    overflow: hidden;
    background: var(--backdrop);
  }
  .canvas {
    position: relative;
    width: 1200px;
    height: 935px;
  }
  .card {
    position: absolute;
    left: 100px;
    top: 182px;
    width: 1000px;
    height: 571px;
    background: var(--card);
    border-radius: 40px;
    overflow: hidden;
    box-shadow: 0 8px 24px rgba(0,0,0,0.18);
  }
  .card-swoosh {
    position: absolute;
    left: 0;
    top: 0;
    width: 1000px;
    height: 571px;
  }
  .brand {
    position: absolute;
    left: 300px;
    top: 88px;
    display: flex;
    align-items: center;
    gap: 18px;
  }
  .brand-dot {
    width: 34px;
    height: 34px;
    border-radius: 50%;
    background: var(--brand-grey);
  }
  .brand-name {
    font-family: "Arimo", sans-serif;
    font-weight: 700;
    font-size: 48px;
    color: var(--brand-grey);
    line-height: 1;
  }
  .contact {
    position: absolute;
    left: 405px;
    top: 200px;
    font-family: "Arimo", sans-serif;
    font-size: 22px;
    line-height: 29px;
    color: var(--text-grey);
  }
  .contact p { margin: 0; }
  .contact .label {
    color: var(--brand-green-dark);
    font-weight: 700;
  }
  .person {
    position: absolute;
    right: 626px;
    top: 318px;
    font-family: "Arimo", sans-serif;
    text-align: right;
  }
  .person-name {
    margin: 0;
    font-size: 28px;
    font-weight: 700;
    color: var(--brand-green-dark);
  }
  .person-title {
    margin: 4px 0 0;
    font-size: 18px;
    color: var(--text-grey);
  }
</style>
</head>
<body>
<div class="canvas">
  <div class="card">
    <svg class="card-swoosh" viewBox="0 0 1000 571" aria-hidden="true">
      <path d="M0 380 C 60 470, 140 540, 260 571 L 0 571 Z" fill="var(--band-grey)"/>
      <path d="M0 395 C 50 480, 115 540, 215 571 L 0 571 Z" fill="var(--brand-green)"/>
    </svg>

    <div class="brand">
      <div class="brand-dot"></div>
      <div class="brand-name">Meridow Air</div>
    </div>

    <div class="person">
      <p class="person-name">Samuel K Orlowski</p>
      <p class="person-title">Founder</p>
    </div>

    <div class="contact">
      <p>The Halvern Tower</p>
      <p>482 Tamsin Ridge Rd. Suite 210</p>
      <p>Westlake, OH 44718</p>
      <p><span class="label">Phone :</span> 440-555-0142</p>
      <p><span class="label">Cell &nbsp;:</span> 216-555-0187</p>
      <p><span class="label">Fax &nbsp;:</span> 440-555-0163</p>
      <p><span class="label">License No :</span> Air Carrier #4RXB519T</p>
      <p><span class="label">Email :</span> sorlowski@meridowair.example</p>
      <p><span class="label">Web &nbsp;:</span> www.meridowair.example</p>
    </div>
  </div>
</div>
</body>
</html>
```